Sharpen Your Calling book cover and updated company logo bundle

USE THE LOGO ON THE BACK COVER. I WANT AN UPDATED LOOK TO MY LOGO
Size of book: 5.5 x 8.5
Title: Sharpen Your Calling
Subtitle: An introvert’s guide to creating a coaching business that reflects who you are
The Subtitle does NOT go on the book cover
Author: Marla Trundell
BOOK DESCRIPTION: This book will help coaches and creative professionals get confidently clear on who they are so they can create a business that reflects their inner message.

DEMOGRAPHICS — Coaches and creative professional age 35-45

WOULD YOU PREFER PEOPLE OR OBJECTS ON YOUR COVER?
Objects or abstract designs
Anything I don’t want on the cover? people
Objects or symbols I want on the cover: possibly magnifying glass

IF YOU HAVE ANY PHOTOS THAT YOU WOULD LIKE US TO USE, PLEASE INCLUDE THE LINK(S) HERE. My logo or face pic for the back cover (Face pic pending)

COPY FOR THE SPINE
Sharpen Your Calling
Marla Trundell
Lantern Hill Press (with logo)

COPY FOR THE BACK COVER (270 words) my biz logo at the bottom and my picture next to my short bio. (Picture to come)

Create a Coaching Business that Reflects Who You Are

Do you want to step confidently into your new career by doing what you love? You aren't alone! But instead of doing what they love, many new coaches get stuck by trying to fit into traditional ways of doing business and create many unnecessary hurdles to happiness and success.
In this book, creative business coach, Marla Trundell teaches you, as she has taught herself and many others, to stop feeling guilty about what you “should” do in your life and in the process you will learn how to turn your passion into a purposeful career.

New coaches will learn how to:
• Recognize how your life decisions to this point are holding you back.
• Discover your gifts so you can express yourself through your creative projects.
• Identify and develop tools to bring your passion into purpose
• Offer services based on what you love to do.
• Understand your personal work style and work-flow to optimize your ideas and productivity.
• Create a message that reflects who you are to attract clients to work with you.
• Ask confidently for what you are worth and get it every time.
Join Marla on the journey of reconnecting with yourself and manifesting your dream.

Marla Trundell, founder of Harbor Heart and Soul, helps new coaches and creative entrepreneurs find their inner voice so that they have the confidence to bring their authentic selves out into the world. Marla has gone through this process for herself and helped other new businesses achieve dramatic improvements in their organization and focus as a result.

Target Market(s)

indicated in description

Industry/Entity Type

Life Coaching

Logo Text

Harbor Heart and Soul

Requirements
Must have
• updated look on existing logo it is going on the back of the book
Nice to have
• I like the font in the book cover I attached but Id like to see what else is possible

```html
<!DOCTYPE html>
<html lang="en">
<head>
<meta charset="utf-8">
<title>Sharpen Your Calling – Book Cover</title>
<link href="https://fonts.googleapis.com/css2?family=Federo&family=Roboto+Condensed:ital,wght@0,400;1,400&family=Sedgwick+Ave+Display&family=Montserrat:wght@600&display=swap" rel="stylesheet">
<style>
  :root {
    --rust: #b03a1c;
    --wine: #8a1c1c;
    --olive: #6f7a1e;
    --ink: #1d1d1d;
    --paper: #ffffff;
    --desk-light: #e6e2dc;
    --desk-mid: #d2ccc4;
    --lens: rgba(250, 250, 248, 0.95);
    --screen: rgba(60, 60, 62, 0.75);
    --keys: rgba(252, 252, 252, 0.95);
    --pot: rgba(120, 170, 140, 0.75);
    --leaf: rgba(150, 200, 60, 0.7);
    --notebook: rgba(190, 160, 120, 0.8);
    --placeholder: #5e5e5e;
    --logo-orange: #e8751a;
  }
  * { margin: 0; padding: 0; box-sizing: border-box; }
  html, body { width: 1200px; height: 915px; overflow: hidden; background: var(--paper); }
  .cover { position: relative; width: 1200px; height: 915px; overflow: hidden; background: var(--paper); }

  /* front cover photo area */
  .desk-scene {
    position: absolute; left: 500px; top: 0; width: 700px; height: 915px;
    background:
      linear-gradient(90deg, var(--paper) 0%, rgba(255,255,255,0.85) 5%, rgba(255,255,255,0) 14%),
      radial-gradient(circle at 328px 392px, var(--lens) 0, var(--lens) 88px, rgba(255,255,255,0) 112px),
      radial-gradient(ellipse 150px 110px at 500px 520px, var(--screen) 0, rgba(60,60,62,0) 100%),
      radial-gradient(ellipse 170px 90px at 170px 820px, var(--keys) 0, rgba(255,255,255,0) 100%),
      radial-gradient(ellipse 130px 110px at 500px 810px, var(--pot) 0, rgba(120,170,140,0) 100%),
      radial-gradient(ellipse 90px 50px at 490px 780px, var(--leaf) 0, rgba(150,200,60,0) 100%),
      radial-gradient(ellipse 60px 160px at 670px 680px, var(--notebook) 0, rgba(190,160,120,0) 100%),
      linear-gradient(160deg, var(--desk-light) 0%, var(--desk-mid) 100%);
  }

  /* back cover */
  .back { position: absolute; left: 53px; top: 0; width: 500px; color: var(--ink);
    font-family: "Roboto Condensed", "Arial Narrow", sans-serif; font-size: 15.5px; line-height: 19.2px; }
  .back-heading { position: absolute; left: 0; font-family: "Federo", serif; font-weight: 400;
    color: var(--wine); font-size: 21.5px; white-space: nowrap; }
  .back-heading.lead { top: 64px; }
  .back-heading.learn { top: 278px; }
  .blurb { position: absolute; top: 104px; left: 0; width: 494px; }
  .learn-list { position: absolute; top: 301px; left: 0; width: 494px; list-style: none; }
  .learn-list li::before { content: "• "; }
  .invite { position: absolute; top: 476px; left: 0; width: 494px; text-align: center;
    font-style: italic; font-size: 18.5px; line-height: 24px; }

  .author-photo { position: absolute; left: 48px; top: 538px; width: 136px; height: 179px;
    background: var(--placeholder); color: var(--wine); font-family: "Roboto Condensed", sans-serif;
    font-size: 15px; display: flex; align-items: center; justify-content: center; }
  .author-bio { position: absolute; left: 198px; top: 556px; width: 356px; color: var(--wine);
    font-family: "Roboto Condensed", sans-serif; font-style: italic; font-size: 15.5px; line-height: 19.2px; }

  .client-logo { position: absolute; left: 56px; top: 778px; display: flex; align-items: center; gap: 12px;
    font-family: "Federo", serif; font-size: 27px; color: var(--logo-orange); white-space: nowrap; }
  .client-logo .dot { width: 40px; height: 40px; border-radius: 50%; background: var(--logo-orange); }

  /* spine */
  .spine-text { position: absolute; writing-mode: vertical-rl; font-family: "Federo", serif;
    font-size: 17px; color: var(--wine); white-space: nowrap; }
  .spine-title { left: 589px; top: 44px; }
  .spine-author { left: 589px; top: 266px; }
  .spine-publisher { position: absolute; left: 588px; top: 722px; writing-mode: vertical-rl;
    display: flex; align-items: center; gap: 8px; font-family: "Roboto Condensed", sans-serif;
    font-size: 17px; color: var(--ink); white-space: nowrap; }
  .spine-publisher .mark { width: 18px; height: 18px; border-radius: 50%; background: var(--ink); }

  /* front cover */
  .title { position: absolute; left: 650px; top: 58px; width: 510px; text-align: center;
    font-family: "Sedgwick Ave Display", cursive; font-size: 140px; line-height: 140px; color: var(--rust); }
  .title-rule { position: absolute; top: 194px; height: 7px; background: var(--rust); }
  .title-rule.left { left: 664px; width: 168px; }
  .title-rule.right { left: 928px; width: 132px; }
  .subtitle { position: absolute; left: 674px; top: 224px; width: 470px; font-family: "Montserrat", sans-serif;
    font-weight: 600; font-size: 42px; line-height: 46px; letter-spacing: 11px; color: var(--olive); white-space: nowrap; }
  .author-band { position: absolute; left: 612px; top: 828px; width: 588px; height: 46px; background: var(--rust);
    display: flex; align-items: center; justify-content: center; }
  .author-band span { font-family: "Federo", serif; font-size: 37px; line-height: 46px; color: var(--paper); }
</style>
</head>
<body>
<div class="cover">
  <div class="desk-scene" role="img" aria-label="Photo of a light wooden desk with a magnifying glass over an idea light bulb note, a white smartphone, keyboard, spiral notebook and a green cup of pencils"></div>

  <section class="back">
    <h2 class="back-heading lead">Create a Coaching Business that Reflects Who You Are</h2>
    <p class="blurb">Do you want to step confidently into your new career by doing what you love? You aren't alone! But instead of doing what they love, many new coaches get stuck by trying to fit into traditional ways of doing business and create many un&shy;necessary hurdles to happiness and success.<br>In this book, creative business coach, Marla Trundell teaches you, as she has taught herself and many others, to stop feeling guilty about what you “should” do in your life and in the process you will learn how to turn your passion into a purposeful career.</p>
    <h3 class="back-heading learn">New coaches will learn how to:</h3>
    <ul class="learn-list">
      <li>Recognize how your life decisions to this point are holding you back.</li>
      <li>Discover your gifts so you can express yourself through your creative projects.</li>
      <li>Identify and develop tools to bring your passion into purpose</li>
      <li>Offer services based on what you love to do.</li>
      <li>Understand your personal work style and work-flow to optimize your ideas and productivity.</li>
      <li>Create a message that reflects who you are to attract clients to work with you.</li>
      <li>Ask confidently for what you are worth and get it every time.</li>
    </ul>
    <p class="invite">Join Marla on the journey of reconnecting with yourself<br>and manifesting your dream.</p>
  </section>

  <div class="author-photo">photo</div>
  <p class="author-bio">Marla Trundell, founder of Harbor Heart and Soul, helps new coaches and creative entrepreneurs find their inner voice so that they have the confidence to bring their authentic selves out into the world. Marla has gone through this process for herself and helped other new businesses achieve dramatic improvements in their organization and focus as a result.</p>

  <div class="client-logo"><span class="dot"></span>Harbor Heart and Soul</div>

  <div class="spine-text spine-title">Sharpen Your Calling</div>
  <div class="spine-text spine-author">Marla Trundell</div>
  <div class="spine-publisher"><span class="mark"></span>Lantern Hill Press</div>

  <h1 class="title">Sharpen</h1>
  <div class="title-rule left"></div>
  <div class="title-rule right"></div>
  <div class="subtitle">YOUR CALLING</div>

  <div class="author-band"><span>Marla Trundell</span></div>
</div>
</body>
</html>
```